Label to go onto food packaging.

We need to create a visually interesting and appealing label to stick onto our take away food packaging. The label should contain information of the food products our cafe sells. The label is to go onto biodegradable food bowls and clam shell packaging.
The information is basically the lines we sell - buddha bowls, super smoothies, vegan burgers and curries. And also the slogan 'nourish and refresh'. We have a logo design that we would like to incorporate onto the label (but not essential)
The design will go onto a rectangle strip label.
The colours of our food outlet are splashes of yellow, blue and grey in a white interior.
We also feature a large garden green wall. You may view images from our instagram page bright pebble kitchen

Target Market(s)

Young professional, health conscious, plant based eaters. To be used on takeaway packaging.

Industry/Entity Type

Food Production

Font styles to use
Sans Serif

Colors

Designer to choose colors to be used in the design.

Requirements
Must have
• Bold, appealing, informative.
Nice to have
• Logo incorporated, possibly as a watermark?
Should not have
• No floral shapes. If incorporating the logo, use a circle or nothing around it. No pictures/photos of food

```html
<!DOCTYPE html>
<html lang="en">
<head>
<meta charset="utf-8">
<title>Bright Pebble Kitchen – Takeaway Labels</title>
<link rel="stylesheet" href="https://fonts.googleapis.com/css2?family=Montserrat:wght@600;700&family=Signika:wght@700&family=Norican&display=swap">
<style>
  :root {
    --navy: #0b2548;
    --grey: #8f959c;
    --ray: #d3d5d9;
    --paper: #ffffff;
    --canvas: #ffffff;
    --blue: #3bb3e6;
    --red: #e4412f;
    --green: #8dc44a;
    --yellow: #fcc93f;
  }
  * { box-sizing: border-box; margin: 0; padding: 0; }
  html, body {
    width: 972px;
    height: 1200px;
    overflow: hidden;
    background: var(--canvas);
  }
  .sheet {
    position: relative;
    width: 972px;
    height: 1200px;
  }
  .label {
    position: absolute;
    left: 122px;
    width: 727px;
    height: 194px;
    background: var(--paper);
    box-shadow: 0 1px 4px rgba(0,0,0,0.22);
    overflow: hidden;
  }
  .label--bowl { top: 43px; --accent: var(--blue); }
  .label--curry { top: 273px; --accent: var(--red); }
  .label--burger { top: 503px; --accent: var(--green); }
  .label--smoothie { top: 732px; --accent: var(--yellow); }
  .label--blank { top: 962px; --accent: var(--yellow); }

  .label__brand {
    position: absolute;
    left: 37px;
    top: 33px;
    width: 128px;
    height: 128px;
    border: 3px solid var(--grey);
    border-radius: 50%;
    display: flex;
    align-items: center;
    justify-content: center;
    text-align: center;
    font-family: "Montserrat", sans-serif;
    font-weight: 700;
    font-size: 14px;
    line-height: 1.1;
    letter-spacing: 0.04em;
    text-transform: uppercase;
    color: var(--grey);
  }
  .label__brace {
    position: absolute;
    left: 0;
    top: 0;
    width: 727px;
    height: 194px;
  }
  .label__burst {
    position: absolute;
    left: 0;
    top: 0;
    width: 727px;
    height: 194px;
  }
  .label__copy {
    position: absolute;
    left: 228px;
    width: 460px;
    top: 0;
    height: 194px;
    text-align: center;
    color: var(--navy);
  }
  .label__slogan {
    position: absolute;
    left: 0; right: 0;
    top: 40px;
    font-family: "Montserrat", sans-serif;
    font-weight: 700;
    font-size: 22px;
    letter-spacing: 0.02em;
  }
  .label__product {
    position: absolute;
    left: 0; right: 0;
    top: 62px;
    font-family: "Signika", sans-serif;
    font-weight: 700;
    font-size: 60px;
    line-height: 1.1;
    letter-spacing: -0.005em;
  }
  .label__tagline {
    position: absolute;
    left: 0; right: 0;
    top: 135px;
    font-family: "Norican", cursive;
    font-size: 23px;
  }
</style>
</head>
<body>
<main class="sheet">

  <section class="label label--bowl">
    <svg class="label__burst" viewBox="0 0 727 194" aria-hidden="true"><circle cx="457" cy="97" r="196" fill="none" stroke="var(--ray)" stroke-width="70"/></svg>
    <div class="label__brand">Bright<br>Pebble<br>Kitchen</div>
    <svg class="label__brace" viewBox="0 0 727 194" aria-hidden="true"><path d="M160 2 C178 2 185 12 185 30 L185 80 C185 91 195 97 214 97 C195 97 185 103 185 114 L185 164 C185 182 178 192 160 192" fill="none" stroke="var(--accent)" stroke-width="6"/></svg>
    <div class="label__copy">
      <p class="label__slogan">NOURISH &amp; REFRESH</p>
      <h2 class="label__product">Buddha Bowl</h2>
      <p class="label__tagline">Nutrient dense whole foods</p>
    </div>
  </section>

  <section class="label label--curry">
    <svg class="label__burst" viewBox="0 0 727 194" aria-hidden="true"><circle cx="457" cy="97" r="196" fill="none" stroke="var(--ray)" stroke-width="70"/></svg>
    <div class="label__brand">Bright<br>Pebble<br>Kitchen</div>
    <svg class="label__brace" viewBox="0 0 727 194" aria-hidden="true"><path d="M160 2 C178 2 185 12 185 30 L185 80 C185 91 195 97 214 97 C195 97 185 103 185 114 L185 164 C185 182 178 192 160 192" fill="none" stroke="var(--accent)" stroke-width="6"/></svg>
    <div class="label__copy">
      <p class="label__slogan">NOURISH &amp; REFRESH</p>
      <h2 class="label__product">Curry</h2>
      <p class="label__tagline">Nutrient dense whole foods</p>
    </div>
  </section>

  <section class="label label--burger">
    <svg class="label__burst" viewBox="0 0 727 194" aria-hidden="true"><circle cx="457" cy="97" r="196" fill="none" stroke="var(--ray)" stroke-width="70"/></svg>
    <div class="label__brand">Bright<br>Pebble<br>Kitchen</div>
    <svg class="label__brace" viewBox="0 0 727 194" aria-hidden="true"><path d="M160 2 C178 2 185 12 185 30 L185 80 C185 91 195 97 214 97 C195 97 185 103 185 114 L185 164 C185 182 178 192 160 192" fill="none" stroke="var(--accent)" stroke-width="6"/></svg>
    <div class="label__copy">
      <p class="label__slogan">NOURISH &amp; REFRESH</p>
      <h2 class="label__product">Vegan Burger</h2>
      <p class="label__tagline">Nutrient dense whole foods</p>
    </div>
  </section>

  <section class="label label--smoothie">
    <svg class="label__burst" viewBox="0 0 727 194" aria-hidden="true"><circle cx="457" cy="97" r="196" fill="none" stroke="var(--ray)" stroke-width="70"/></svg>
    <div class="label__brand">Bright<br>Pebble<br>Kitchen</div>
    <svg class="label__brace" viewBox="0 0 727 194" aria-hidden="true"><path d="M160 2 C178 2 185 12 185 30 L185 80 C185 91 195 97 214 97 C195 97 185 103 185 114 L185 164 C185 182 178 192 160 192" fill="none" stroke="var(--accent)" stroke-width="6"/></svg>
    <div class="label__copy">
      <p class="label__slogan">NOURISH &amp; REFRESH</p>
      <h2 class="label__product">Super Smoothie</h2>
      <p class="label__tagline">Nutrient dense whole foods</p>
    </div>
  </section>

  <section class="label label--blank">
    <div class="label__brand">Bright<br>Pebble<br>Kitchen</div>
    <svg class="label__brace" viewBox="0 0 727 194" aria-hidden="true"><path d="M160 2 C178 2 185 12 185 30 L185 80 C185 91 195 97 214 97 C195 97 185 103 185 114 L185 164 C185 182 178 192 160 192" fill="none" stroke="var(--accent)" stroke-width="6"/></svg>
  </section>

</main>
</body>
</html>
```